vortane realty business card

We need a Business card for our new business. The logo was designed by ArtQuillo, and the text We want on the back is:
REAL ESTATE INVESTMENTS
- BUY, RENOVATE, SELL AND RENT RESIDENTIAL PROPERTIES
- FULL HOME REHABBING , REMODELING AND INTERIOR DESIGN
- HOME STAGING SERVICES
- WHOLESALE INVESTOR PROPERTIES
- MAKE CASH OFFERS ON HOUSES IN ANY CONDITION AND IN ANY SITUATION
- PRIVATE MONEY INVESTOR PROGRAMS WITH 6-12% RETURNS
- PAY CASH REWARDS FOR REFFERALS
- CONCIERGE SERVICE

```html
<!DOCTYPE html>
<html lang="en">
<head>
<meta charset="utf-8">
<title>Vortane Realty – Business Card</title>
<link rel="stylesheet" href="https://fonts.googleapis.com/css2?family=Barlow:wght@300;400;500;700&display=swap">
<style>
  :root {
    --bg: #d9d9d9;
    --card-white: #ffffff;
    --ink: #2b2b2b;
    --ink-soft: #8a8a8a;
    --band-dark: #1c1c1c;
    --band-dark-2: #262626;
    --teal: #6cc3cc;
    --teal-deep: #4fb0ba;
    --back-text: #b9b9b9;
  }
  * { box-sizing: border-box; margin: 0; padding: 0; }
  html, body {
    width: 1200px; height: 861px; overflow: hidden;
    background: var(--bg);
    font-family: "Barlow", Arial, sans-serif;
  }
  .stage { position: relative; width: 1200px; height: 861px; }

  .card {
    position: absolute;
    width: 520px; height: 300px;
    border-radius: 4px;
    overflow: hidden;
    box-shadow: 0 10px 24px rgba(0,0,0,.18), 0 2px 4px rgba(0,0,0,.12);
  }
  .card-front { left: 50px; top: 150px; background: var(--card-white); }
  .card-back  { left: 630px; top: 410px; background: var(--band-dark); }

  .card-shapes { position: absolute; inset: 0; }

  /* Front */
  .holder { position: absolute; left: 62px; top: 62px; }
  .holder-name {
    font-weight: 700; font-size: 26px; letter-spacing: 1px;
    color: var(--ink); text-transform: uppercase; line-height: 1;
  }
  .holder-title { font-weight: 400; font-size: 15px; color: var(--ink-soft); margin-top: 4px; }

  .brand-front { position: absolute; right: 26px; top: 26px; text-align: left; }
  .brand-name { color: var(--teal-deep); font-weight: 400; font-size: 22px; line-height: 1; letter-spacing: .5px; }
  .brand-tag { color: var(--ink-soft); font-size: 10px; letter-spacing: 1.6px; margin-top: 3px; }

  .contact {
    position: absolute; display: flex; align-items: center; gap: 7px;
    color: #ffffff; font-size: 12px; font-weight: 500; white-space: nowrap;
    line-height: 17px;
  }
  .contact svg { width: 17px; height: 17px; flex: none; }
  .c-fax   { left: 340px; top: 104px; }
  .c-phone { left: 190px; top: 149px; }
  .c-email { left: 340px; top: 149px; }
  .c-addr  { left: 206px; top: 174px; }
  .c-web   { left: 312px; top: 214px; }

  /* Back */
  .back-band {
    position: absolute; left: 0; right: 0; top: 100px; height: 104px;
    background: var(--card-white);
    display: flex; align-items: center; justify-content: center; gap: 14px;
  }
  .brand-mark { width: 30px; height: 30px; background: var(--teal); flex: none; }
  .brand-back .brand-name { font-size: 36px; }
  .brand-back .brand-tag { font-size: 15px; letter-spacing: 2.4px; margin-top: 4px; }

  .services {
    position: absolute; left: 0; right: 0;
    text-align: center; color: var(--back-text);
    font-size: 10px; font-weight: 500; letter-spacing: 1px;
    line-height: 15px; text-transform: uppercase;
  }
  .services-top { top: 38px; }
  .services-bottom { top: 220px; }
  .dot { color: var(--teal); }
</style>
</head>
<body>
<main class="stage">

  <section class="card card-front" aria-label="Business card front">
    <svg class="card-shapes" viewBox="0 0 520 300" aria-hidden="true">
      <polygon points="40,72 54,72 54,116 92,116 92,130 40,130" fill="var(--teal)"/>
      <polygon points="0,196 170,196 230,240 520,240 520,262 0,262" fill="var(--teal)"/>
      <polygon points="330,96 520,96 520,130 316,130" fill="var(--band-dark)"/>
      <polygon points="150,140 520,140 520,200 200,200" fill="var(--band-dark-2)"/>
      <polygon points="258,208 520,208 520,238 296,238" fill="var(--band-dark)"/>
    </svg>

    <div class="holder">
      <p class="holder-name">Marcus Ellery</p>
      <p class="holder-title">General Manager</p>
    </div>

    <div class="brand-front">
      <p class="brand-name">VORTANE Realty</p>
      <p class="brand-tag">REAL ESTATE SOLUTIONS</p>
    </div>

    <p class="contact c-fax">
      <svg viewBox="0 0 17 17" aria-hidden="true"><rect width="17" height="17" rx="3" fill="var(--teal)"/><rect x="4" y="6" width="9" height="7" rx="1" fill="#fff"/><rect x="6" y="3" width="5" height="4" fill="#fff"/></svg>
      (00) 123 4567
    </p>
    <p class="contact c-phone">
      <svg viewBox="0 0 17 17" aria-hidden="true"><rect width="17" height="17" rx="3" fill="var(--teal)"/><path d="M5 4 L7 4 L8 7 L6.8 8 Q8 10 9.5 10.5 L10.5 9.3 L13 10.5 L13 12.5 Q7 13 4.5 6 Z" fill="#fff"/></svg>
      (00) 123 4567
    </p>
    <p class="contact c-email">
      <svg viewBox="0 0 17 17" aria-hidden="true"><rect width="17" height="17" rx="3" fill="var(--teal)"/><rect x="3.5" y="5" width="10" height="7" fill="#fff"/><path d="M3.5 5 L8.5 9 L13.5 5" stroke="var(--teal)" fill="none"/></svg>
      name@vortanerealty.com
    </p>
    <p class="contact c-addr">
      <svg viewBox="0 0 17 17" aria-hidden="true"><rect width="17" height="17" rx="3" fill="var(--teal)"/><path d="M8.5 14 Q4.5 9 4.5 7 A4 4 0 0 1 12.5 7 Q12.5 9 8.5 14 Z" fill="#fff"/><circle cx="8.5" cy="7" r="1.5" fill="var(--teal)"/></svg>
      123 Lorem Avenue, Dummy Text 45678, Ipsum
    </p>
    <p class="contact c-web">
      <svg viewBox="0 0 17 17" aria-hidden="true"><rect width="17" height="17" rx="3" fill="var(--teal)"/><circle cx="8.5" cy="8.5" r="4.5" fill="#fff"/><path d="M7 6 L11 8.5 L7 11 Z" fill="var(--teal)"/></svg>
      vortanerealty.com
    </p>
  </section>

  <section class="card card-back" aria-label="Business card back">
    <p class="services services-top">
      <span class="dot">•</span> Buy, renovate, sell and rent residential properties <span class="dot">•</span> Full home<br>
      rehabbing, remodeling and interior design <span class="dot">•</span> Home staging services<br>
      <span class="dot">•</span> Wholesale investor properties <span class="dot">•</span>
    </p>

    <div class="back-band">
      <span class="brand-mark" aria-hidden="true"></span>
      <div class="brand-back">
        <p class="brand-name">VORTANE Realty</p>
        <p class="brand-tag">REAL ESTATE SOLUTIONS</p>
      </div>
    </div>

    <p class="services services-bottom">
      <span class="dot">•</span> Make cash offers on houses in any condition and in any situation<br>
      <span class="dot">•</span> Private money investor programs with 6-12% returns <span class="dot">•</span> Pay cash<br>
      rewards for refferals <span class="dot">•</span> Concierge service <span class="dot">•</span>
    </p>
  </section>

</main>
</body>
</html>
```